Tea Sorama Matcha packaging. Matcha from Japan, by Japanese.

Our company, Soramacrafts.example.jp is a company steeped in Japanese traditional festival products for nearly 100 years. Located in Yame, Japan's famous tea region. We now create a new branch in our business, starting with matcha.

We need a contemporary yet reflect the tradition of our products design for matcha packaging. This design is aimed at young US consumer.

We will have 6 different types of matcha, each at different grade and price point. We would like to use colour and product name to differentiate between them. Product name shall include the grade of matcha: culinary, premium or ceremonial; and a Japanese name such as Tomuro, Serino ...; and a short description blended matcha or first harvest from either Uji, Kagoshima or Yame region.

The design should have information panel at the back for US market. Please refer to the sample design in the attachment.

Size of matcha pouch
2 sizes
12 x 15 cm
12 x 19.5cm

Please note the logo can be custom and change to fit the design. But it must have Sorama's family crest on it, with or without the circle.

Target Market(s)

US market

Industry/Entity Type

Food and Drink

Requirements
Must have
• As we have 6 different matcha, they shall be somehow differentiated between them, possibly by colour.
Nice to have
• As our company traditionally making Kabuto, Hina Ningyo ...., if you can include a mas

```html
<!DOCTYPE html>
<html lang="en">
<head>
<meta charset="utf-8">
<title>Tea Sorama Matcha Pouch Range</title>
<link rel="stylesheet" href="https://fonts.googleapis.com/css2?family=Cinzel:wght@700&family=Lexend:wght@300;400;500;600&family=Noto+Serif+SC:wght@500&display=swap">
<style>
  :root {
    --page: #ffffff;
    --pouch: #ededed;
    --ink: #111111;
    --leaf-dark: #2f6a12;
    --leaf-mid: #5aa21e;
    --leaf-light: #a9d74a;
    --culinary: #b0890f;
    --culinary-script: #c4891c;
    --premium: #0c2b17;
    --premium-script: #1f4a2a;
    --ceremonial: #2c0505;
    --ceremonial-script: #4b1313;
    --badge: #2a6b2a;
    --on-band: #f2eee6;
  }
  * { box-sizing: border-box; margin: 0; padding: 0; }
  html, body { width: 1200px; height: 609px; overflow: hidden; background: var(--page); }
  .range { position: relative; width: 1200px; height: 609px; }

  .pouch {
    position: absolute; top: 84px; width: 362px; height: 452px;
    background: var(--pouch);
    box-shadow: 0 14px 12px -8px rgba(0,0,0,0.18);
    overflow: hidden;
  }
  .pouch--culinary { left: 31px; --tone: var(--culinary); --script: var(--culinary-script); }
  .pouch--premium { left: 420px; --tone: var(--premium); --script: var(--premium-script); }
  .pouch--ceremonial { left: 810px; --tone: var(--ceremonial); --script: var(--ceremonial-script); }

  .leaf-art {
    position: absolute; left: 0; top: 10px; width: 242px; height: 300px;
    border-radius: 0 70% 60% 0 / 0 45% 55% 0;
    background: linear-gradient(150deg, var(--leaf-mid) 0%, var(--leaf-dark) 45%, var(--leaf-mid) 75%, var(--leaf-light) 100%);
  }

  .brand { position: absolute; left: 128px; top: 20px; width: 110px; text-align: center; }
  .brand__mark {
    display: block; width: 50px; height: 50px; margin: 2px auto 0;
    border-radius: 50%; border: 4px solid var(--ink);
  }
  .brand__name {
    display: block; margin-top: 3px; white-space: nowrap;
    font-family: "Cinzel", serif; font-weight: 700; font-size: 15px;
    color: var(--ink); letter-spacing: 0;
  }

  .script {
    position: absolute; display: flex; flex-direction: column;
    font-family: "Noto Serif SC", serif; font-weight: 500; color: var(--script);
    line-height: 1;
  }
  .script--first { left: 264px; top: 44px; font-size: 32px; gap: 3px; }
  .script--second { left: 305px; top: 78px; font-size: 27px; gap: 3px; }

  .grade {
    position: absolute; right: 25px; top: 270px;
    font-family: "Lexend", sans-serif; font-weight: 600; font-size: 15.5px;
    color: var(--ink); letter-spacing: 0.2px;
  }

  .band {
    position: absolute; left: 139px; top: 294px; width: 223px; height: 125px;
    background: var(--tone); color: var(--on-band);
    font-family: "Lexend", sans-serif;
  }
  .band__cultivar {
    position: absolute; left: 12px; top: 11px;
    font-weight: 300; font-size: 21px; line-height: 24.5px; letter-spacing: 0.3px;
  }
  .band__tagline {
    position: absolute; left: 15px; top: 92px;
    font-weight: 300; font-size: 8.2px; line-height: 11px; opacity: 0.9;
  }
  .band__weight {
    position: absolute; right: 28px; top: 99px; text-align: center;
    font-weight: 400; font-size: 8.5px; line-height: 9px;
  }

  .uses {
    position: absolute; right: 228px; top: 362px; text-align: right;
    font-family: "Lexend", sans-serif; font-weight: 500; font-size: 7.6px;
    line-height: 11.2px; color: var(--ink);
  }

  .certs { position: absolute; left: 13px; top: 400px; display: flex; align-items: center; gap: 3px; }
  .cert--round { width: 24px; height: 24px; border-radius: 50%; border: 2px solid var(--badge); background: #ffffff; }
  .cert--oval { width: 39px; height: 20px; border-radius: 10px; border: 2px solid var(--badge); }
  .cert--block { width: 54px; height: 20px; background: var(--ink); }
</style>
</head>
<body>
<main class="range">

  <section class="pouch pouch--culinary">
    <div class="leaf-art" role="img" aria-label="Illustration of fresh green tea leaves on a stem"></div>
    <div class="brand"><span class="brand__mark"></span><span class="brand__name">TEA SORAMA</span></div>
    <div class="script script--first" lang="zh"><span>津</span><span>喜</span><span>先</span><span>生</span><span>谊</span><span>喜</span></div>
    <div class="script script--second" lang="zh"><span>来</span><span>生</span><span>由</span><span>时</span><span>西</span><span>生</span></div>
    <h2 class="grade">CULINARY</h2>
    <div class="band">
      <p class="band__cultivar">SINGLE<br>CULTIVA<br>OKUMIDORI</p>
      <p class="band__tagline">A naturally potent boost<br>for body mind and spirit</p>
      <p class="band__weight">Net weight<br>1.76oz (50g)</p>
    </div>
    <p class="uses">LATTES, SMOOTHIES,<br>BAKING,HOT OR<br>COLD SHOTS</p>
    <div class="certs"><span class="cert--round"></span><span class="cert--oval"></span><span class="cert--block"></span></div>
  </section>

  <section class="pouch pouch--premium">
    <div class="leaf-art" role="img" aria-label="Illustration of fresh green tea leaves on a stem"></div>
    <div class="brand"><span class="brand__mark"></span><span class="brand__name">TEA SORAMA</span></div>
    <div class="script script--first" lang="zh"><span>津</span><span>喜</span><span>先</span><span>生</span><span>谊</span><span>喜</span></div>
    <div class="script script--second" lang="zh"><span>来</span><span>生</span><span>由</span><span>时</span><span>西</span><span>生</span></div>
    <h2 class="grade">PREMIUM</h2>
    <div class="band">
      <p class="band__cultivar">SINGLE<br>CULTIVA<br>OKUMIDORI</p>
      <p class="band__tagline">A naturally potent boost<br>for body mind and spirit</p>
      <p class="band__weight">Net weight<br>1.76oz (50g)</p>
    </div>
    <p class="uses">LATTES, SMOOTHIES,<br>BAKING,HOT OR<br>COLD SHOTS</p>
    <div class="certs"><span class="cert--round"></span><span class="cert--oval"></span><span class="cert--block"></span></div>
  </section>

  <section class="pouch pouch--ceremonial">
    <div class="leaf-art" role="img" aria-label="Illustration of fresh green tea leaves on a stem"></div>
    <div class="brand"><span class="brand__mark"></span><span class="brand__name">TEA SORAMA</span></div>
    <div class="script script--first" lang="zh"><span>津</span><span>喜</span><span>先</span><span>生</span><span>谊</span><span>喜</span></div>
    <div class="script script--second" lang="zh"><span>来</span><span>生</span><span>由</span><span>时</span><span>西</span><span>生</span></div>
    <h2 class="grade">CEREMONIAL</h2>
    <div class="band">
      <p class="band__cultivar">SINGLE<br>CULTIVA<br>OKUMIDORI</p>
      <p class="band__tagline">A naturally potent boost<br>for body mind and spirit</p>
      <p class="band__weight">Net weight<br>1.76oz (50g)</p>
    </div>
    <p class="uses">LATTES, SMOOTHIES,<br>BAKING,HOT OR<br>COLD SHOTS</p>
    <div class="certs"><span class="cert--round"></span><span class="cert--oval"></span><span class="cert--block"></span></div>
  </section>

</main>
</body>
</html>
```